use my brand and make an elegant business card  with it

Target Market(s)
male and female ' ages 25 to 45 age- who appreciate the highest quality goods, experiences, services, brands and relationships
Industry/Entity Type
Business
Requirements
Must have
- my logo integrated into the design-note the uploaded file
front: just logo and the phrase: New. Trend. Life. Style
back informations:
Mirela Dostan
Director
phone: +1 604 2917345
www.midostan.com
email: mireladostan@midostan.com
the pin of Facebook (F) and tweeter (T)
Nice to have
- contrast of the colors black gold and silver
Should not have
- cartoons or whimsical design

```html
<!DOCTYPE html>
<html lang="en">
<head>
<meta charset="utf-8">
<title>Vel Doria – Business Card</title>
<link rel="stylesheet" href="https://fonts.googleapis.com/css2?family=Cinzel:wght@500&family=Della+Respira&family=Italianno&display=swap">
<style>
  :root {
    --backdrop: #d3cf8e;
    --card-black: #0a0a0a;
    --damask-dark: #141414;
    --damask-mid: #303030;
    --damask-glow: #3a3a3a;
    --silver-light: #b9bcc2;
    --silver-dark: #55585e;
    --silver-text: #c4c4c4;
    --silver-soft: #a8a8a8;
    --gold: #d4a42a;
    --gold-light: #e9c45a;
    --gold-dark: #9c7418;
    --script-ink: #1c1c1e;
  }
  * { margin: 0; padding: 0; box-sizing: border-box; }
  html, body {
    width: 1200px;
    height: 960px;
    overflow: hidden;
    background: var(--backdrop);
  }
  .canvas {
    position: relative;
    width: 1200px;
    height: 960px;
  }
  .card {
    position: absolute;
    left: 285px;
    width: 630px;
    height: 360px;
    background: var(--card-black);
    overflow: hidden;
    box-shadow: 0 10px 28px rgba(60, 55, 20, 0.35);
  }
  .card--front { top: 90px; }
  .card--back { top: 510px; }

  .damask {
    position: absolute;
    inset: 0;
    background:
      radial-gradient(ellipse 55% 60% at 35% 50%, var(--damask-glow) 0%, var(--damask-mid) 25%, var(--damask-dark) 65%, var(--card-black) 100%);
  }
  .card--front .damask {
    background:
      linear-gradient(180deg, rgba(10,10,10,0) 0%, rgba(10,10,10,0) 35%, var(--card-black) 75%),
      radial-gradient(ellipse 60% 70% at 70% 15%, var(--damask-mid) 0%, var(--damask-dark) 55%, var(--card-black) 100%);
  }

  .tagline-band {
    position: absolute;
    left: 0;
    top: 0;
    width: 150px;
    height: 100%;
    background: linear-gradient(180deg, var(--silver-light) 0%, #8e9197 50%, var(--silver-dark) 100%);
    box-shadow: 4px 0 10px rgba(0,0,0,0.6);
  }
  .tagline-band__edge {
    position: absolute;
    left: 0;
    top: 0;
    width: 26px;
    height: 100%;
    background: linear-gradient(90deg, var(--gold-dark) 0%, var(--gold-light) 50%, var(--gold) 100%);
  }
  .tagline {
    position: absolute;
    left: 34px;
    top: 22px;
    width: 112px;
    font-family: "Italianno", cursive;
    font-size: 54px;
    line-height: 58px;
    color: var(--script-ink);
    text-align: center;
    list-style: none;
  }

  .brand-name {
    position: absolute;
    left: 200px;
    top: 78px;
    font-family: "Cinzel", serif;
    font-weight: 500;
    font-size: 68px;
    line-height: 74px;
    letter-spacing: 2px;
    color: var(--gold);
  }

  .contact {
    position: absolute;
    left: 315px;
    top: 60px;
    font-family: "Della Respira", serif;
    color: var(--silver-text);
    font-style: normal;
  }
  .contact__name {
    font-size: 22px;
    letter-spacing: 1px;
    line-height: 30px;
  }
  .contact__role {
    font-size: 22px;
    letter-spacing: 1px;
    line-height: 30px;
    margin-bottom: 4px;
  }
  .contact__line {
    font-size: 14px;
    line-height: 20px;
    color: var(--silver-soft);
  }
</style>
</head>
<body>
<main class="canvas">
  <section class="card card--front" aria-label="Business card front">
    <div class="damask" role="img" aria-label="Dark black damask floral pattern across the card"></div>
    <div class="tagline-band">
      <div class="tagline-band__edge"></div>
      <ul class="tagline">
        <li>New</li>
        <li>Trend</li>
        <li>Life</li>
        <li>Style</li>
      </ul>
    </div>
    <h1 class="brand-name">VEL<br>DORIA</h1>
  </section>

  <section class="card card--back" aria-label="Business card back">
    <div class="damask" role="img" aria-label="Dark black damask floral pattern across the card"></div>
    <address class="contact">
      <p class="contact__name">Mirela Dostan</p>
      <p class="contact__role">Director</p>
      <p class="contact__line">phone: +1 604 2917345</p>
      <p class="contact__line">www.midostan.com</p>
      <p class="contact__line">email: mireladostan@midostan.com</p>
    </address>
  </section>
</main>
</body>
</html>
```